Pelican Global Trade & Heritage Forum Landing Page Design

We are a Chinese high-end bespoke business travel company. We want to design a landing page, to promote our brand and business, to attract target clients for business development.

We have own logo, like design in modern simple style, like to sample as attached. Like the Sample 2, use different color to display our business services.

We want to mainly display 7 parts of business:
1. Visa Services
2. International Hotel Reservation
3. Worldwide Flight Tickets Booking
4. Worldwide Travel Arrangement
5. VIP Airport Concierge
6. Duty Free Goods
7. International Business Resources

We imagine design a world map, points out popular countries, cities, and destinations, and combine with our own business resources cities.

Design in modern, business, international style. Thank you. Look forward to cooperate with you.

Target Market(s)

Business Clients and High income private client

Industry/Entity Type

Tourism, Business Travel, International Exchange

Coding

Coded - Design and coding required

Requirements
Must have
• Our logo, large images, design a world map

```html
<!DOCTYPE html>
<html lang="en">
<head>
<meta charset="utf-8">
<title>Pelican Global Trade &amp; Heritage Forum</title>
<link rel="stylesheet" href="https://fonts.googleapis.com/css2?family=Oswald:wght@400;500;600&family=Poppins:wght@400;500;600&display=swap">
<style>
:root{
  --ink:#1c1c1c;
  --text:#555b63;
  --blue:#1a67c9;
  --teal:#27b1b4;
  --green:#7cb342;
  --lime:#9abb3a;
  --yellow:#f2b62b;
  --orange:#f07c3a;
  --footer:#2b2c30;
  --footer-line:#3c3d42;
  --map:#dfe4ea;
  --white:#fff;
}
*{box-sizing:border-box;margin:0;padding:0}
html,body{width:1200px;height:4420px;overflow:hidden}
body{position:relative;background:var(--white);font-family:"Poppins",sans-serif;color:var(--text);font-size:14px}
.abs{position:absolute}
h1,h2,h3{font-family:"Oswald",sans-serif;color:var(--ink);font-weight:500}
.section-title{position:absolute;left:0;width:1200px;text-align:center;font-size:40px;line-height:56px}

/* header */
.brand{left:88px;top:24px;display:flex;align-items:center;gap:10px;z-index:3}
.brand-dot{width:34px;height:34px;border-radius:50%;background:var(--blue)}
.brand-name{font-weight:600;font-size:15px;line-height:1.15;color:var(--blue)}
.main-nav{left:516px;top:52px;display:flex;gap:24px;font-size:12px;font-weight:600;color:var(--white);letter-spacing:.5px;z-index:3}
.call{left:964px;top:40px;display:flex;align-items:center;gap:10px;z-index:3}
.call-icon{width:38px;height:38px;border-radius:50%;background:var(--blue);display:flex;align-items:center;justify-content:center}
.call-text{font-size:11px;line-height:1.4;color:var(--white)}
.call-text b{display:block;font-size:13px}

/* hero */
.hero-photo{left:568px;top:0;width:632px;height:660px;border-bottom-left-radius:40px;background:linear-gradient(160deg,#6f96bb 0%,#c9a88a 45%,#a7664a 70%,#3d5566 100%)}
.hero-title{left:88px;top:176px;width:470px;font-size:60px;line-height:68px;font-weight:600}
.hero-lead{left:88px;top:412px;width:360px;font-size:13px;line-height:1.6}
.search{left:88px;top:482px;width:640px;height:96px;background:var(--white);border-radius:8px;box-shadow:0 12px 34px rgba(20,40,80,.16);display:flex;align-items:center;padding:0 20px;gap:14px;z-index:2}
.field{width:112px}
.field label{display:block;font-size:12px;font-weight:600;color:var(--ink);margin-bottom:6px}
.field span{display:block;border:1px solid #dde2ea;border-radius:4px;padding:7px 9px;font-size:11px;color:#8a9099}
.search-btn{margin-left:auto;background:var(--blue);color:var(--white);font-weight:600;font-size:13px;padding:13px 18px;border-radius:4px}

/* services */
.svc-label{position:absolute;width:170px;text-align:center;font-size:12px;font-weight:500;color:var(--ink);line-height:1.35}

/* enjoy */
.collage-back{left:300px;top:1320px;width:240px;height:440px;border-radius:6px;background:linear-gradient(160deg,#e9d7c4,#b58a66);transform:rotate(6deg)}
.collage-front{left:168px;top:1500px;width:240px;height:380px;border-radius:6px;background:linear-gradient(170deg,#9aa9b8,#4d5b6b);border:6px solid var(--white);box-shadow:0 10px 30px rgba(0,0,0,.18);transform:rotate(-4deg)}
.enjoy-title{left:688px;top:1410px;width:330px;font-size:36px;line-height:44px}
.enjoy-text{left:688px;top:1530px;width:340px;font-size:13px;line-height:1.65}
.btn-blue{left:688px;top:1690px;background:var(--blue);color:var(--white);font-size:12px;font-weight:600;padding:11px 20px;border-radius:3px;letter-spacing:.5px}

/* destinations */
.dest{position:absolute;border-radius:4px}
.dest-link{position:absolute;left:577px;top:2320px;width:46px;height:46px;border-radius:50%;background:var(--white);display:flex;align-items:center;justify-content:center}

/* locations */
.world-map{left:160px;top:2660px;width:940px;height:400px;border-radius:24px;background:linear-gradient(180deg,var(--map) 0%,#e9edf2 100%)}
.city-col{position:absolute;top:3100px;list-style:none;font-size:13px;line-height:26px;color:var(--ink)}
.city-col li::before{content:"";display:inline-block;width:5px;height:5px;border-radius:50%;background:var(--ink);margin-right:8px;vertical-align:middle}

/* testimonial */
.quote-mark{left:268px;top:3360px;font-family:"Oswald",sans-serif;font-size:200px;line-height:1;color:#eef1f5}
.testi-title{left:172px;top:3508px;font-size:34px;line-height:44px}
.testi-text{left:172px;top:3566px;width:380px;font-size:13px;line-height:1.65}
.stars{left:172px;top:3652px}
.testi-name{left:172px;top:3680px;font-size:14px;font-weight:600;color:var(--ink)}
.client-photo{left:680px;top:3400px;width:290px;height:290px;border-radius:50%;background:linear-gradient(170deg,#8fb0c8,#6b8d78 55%,#a6553c)}

/* cta + footer */
.site-footer{left:0;top:3940px;width:1200px;height:480px;background:var(--footer)}
.cta{left:200px;top:3872px;width:800px;height:136px;background:linear-gradient(90deg,#24aeb7,#1a67c9);border-radius:2px;display:flex;align-items:center;padding:0 60px;justify-content:space-between;z-index:2}
.cta h2{color:var(--white);font-size:38px;letter-spacing:.5px}
.cta-btn{background:var(--white);color:var(--ink);font-size:12px;font-weight:600;padding:14px 26px;letter-spacing:.5px}
.foot-brand{left:112px;top:4120px;display:flex;align-items:center;gap:10px}
.foot-brand .brand-dot{background:var(--white)}
.foot-brand .brand-name{color:var(--white)}
.socials{left:112px;top:4212px;display:flex;gap:10px}
.socials span{width:30px;height:30px;border-radius:50%;background:var(--white)}
.foot-col{position:absolute;top:4084px;color:#c7c9cf;font-size:12px;line-height:24px}
.foot-col h3{color:var(--white);font-size:17px;margin-bottom:10px}
.contact-row{display:flex;gap:10px;margin-bottom:8px;line-height:1.5}
.contact-row i{flex:none;width:14px;height:14px;margin-top:3px;border-radius:50%;background:var(--teal)}
.newsletter{position:absolute;left:0;top:118px;width:290px;height:42px;background:var(--white);border-radius:2px;display:flex;align-items:center;justify-content:space-between;padding:0 0 0 14px;color:#8a9099}
.newsletter b{width:42px;height:42px;background:var(--blue);display:flex;align-items:center;justify-content:center}
.copyright{left:0;top:4340px;width:1200px;border-top:1px solid var(--footer-line);padding-top:16px;text-align:center;font-size:12px;color:#c7c9cf}
.to-top{left:1124px;top:4330px;width:40px;height:40px;border-radius:50%;background:var(--blue);display:flex;align-items:center;justify-content:center}
</style>
</head>
<body>

<div class="abs hero-photo" role="img" aria-label="Photograph of a canal city with gondolas and a stone bridge"></div>
<div class="abs brand"><span class="brand-dot"></span><span class="brand-name">Pelican Global<br>Trade &amp; Heritage Forum</span></div>
<nav class="abs main-nav"><span>HOME</span><span>TOURS</span><span>DESTINATION</span><span>ABOUT</span><span>NEWS</span><span>CONTACT</span></nav>
<div class="abs call">
  <span class="call-icon"><svg width="18" height="18" viewBox="0 0 24 24" fill="#fff"><path d="M6.6 10.8a15 15 0 006.6 6.6l2.2-2.2c.3-.3.7-.4 1-.2 1.1.4 2.3.6 3.6.6.6 0 1 .4 1 1V20c0 .6-.4 1-1 1A17 17 0 013 4c0-.6.4-1 1-1h3.5c.6 0 1 .4 1 1 0 1.3.2 2.5.6 3.6.1.3 0 .7-.2 1z"/></svg></span>
  <span class="call-text">Call Now<b>+1-555-0148-220</b></span>
</div>

<h1 class="abs hero-title">Explore the Top Destination of Planet Earth</h1>
<p class="abs hero-lead">It is a long established fact that a reader will be distracted by the readable content...</p>
<form class="abs search">
  <div class="field"><label>Destination</label><span>Where to go?</span></div>
  <div class="field"><label>Check in</label><span>Check in</span></div>
  <div class="field"><label>Check out</label><span>Check out</span></div>
  <div class="field"><label>Guests</label><span>Guests</span></div>
  <span class="search-btn">Search</span>
</form>

<h2 class="section-title" style="top:762px">Our Services</h2>
<svg class="abs" style="left:0;top:880px" width="1200" height="260" viewBox="0 0 1200 260" fill="none">
  <defs><marker id="arrow" markerWidth="8" markerHeight="8" refX="6" refY="4" orient="auto"><path d="M0 0L8 4 0 8z" fill="#9aa3ad"/></marker></defs>
  <g stroke="#9aa3ad" stroke-width="2" marker-end="url(#arrow)">
    <path d="M240 128 Q260 180 292 196"/>
    <path d="M380 170 Q400 120 424 104"/>
    <path d="M496 128 Q516 180 540 196"/>
    <path d="M628 170 Q650 120 676 104"/>
    <path d="M748 128 Q768 180 786 196"/>
    <path d="M872 170 Q895 115 920 96"/>
  </g>
  <g stroke-width="9" fill="#fff">
    <circle cx="212" cy="88" r="40" stroke="#1a67c9"/>
    <circle cx="340" cy="200" r="40" stroke="#27b1b4"/>
    <circle cx="468" cy="88" r="40" stroke="#7cb342"/>
    <circle cx="588" cy="200" r="40" stroke="#f2b62b"/>
    <circle cx="720" cy="88" r="40" stroke="#7cb342"/>
    <circle cx="832" cy="200" r="40" stroke="#27b1b4"/>
    <circle cx="960" cy="76" r="40" stroke="#f07c3a"/>
  </g>
  <rect x="198" y="74" width="28" height="28" rx="4" fill="#1a67c9"/>
  <g fill="#27b1b4"><rect x="326" y="192" width="28" height="20" rx="3"/><rect x="332" y="186" width="16" height="8"/></g>
  <path d="M454 94l28-10-6 16z" fill="#7cb342"/>
  <circle cx="588" cy="200" r="14" fill="#f2b62b"/>
  <circle cx="720" cy="88" r="12" fill="#7cb342"/>
  <rect x="820" y="189" width="24" height="22" rx="3" fill="#27b1b4"/>
  <rect x="948" y="66" width="24" height="20" rx="3" fill="#f07c3a"/>
</svg>
<div class="svc-label" style="left:127px;top:868px">Visa Services</div>
<div class="svc-label" style="left:255px;top:1130px">International Hotel<br>Reservation</div>
<div class="svc-label" style="left:383px;top:852px">Worldwide Flight<br>Tickets Booking</div>
<div class="svc-label" style="left:503px;top:1130px">Worldwide Travel<br>Arrangement</div>
<div class="svc-label" style="left:635px;top:852px">VIP Airport<br>Concierge</div>
<div class="svc-label" style="left:747px;top:1130px">Duty Free Goods</div>
<div class="svc-label" style="left:875px;top:840px">International Business<br>Resources</div>

<div class="abs collage-back" role="img" aria-label="Photograph of a traveller relaxing with a hat and bag"></div>
<div class="abs collage-front" role="img" aria-label="Photograph of passports held in front of a city street"></div>
<h2 class="abs enjoy-title">We Make Your Travel More Enjoyable</h2>
<p class="abs enjoy-text">It is a long established fact that a reader will be distracted by the readable content of a page when looking at its layout. The point of using Lorem Ipsum is that it has a more-or-less normal distribution of letters, as opposed to using 'Content here, content here', making it look...</p>
<span class="abs btn-blue">READ MORE</span>

<h2 class="section-title" style="top:1924px">Popular Destinations</h2>
<div class="dest" style="left:88px;top:2000px;width:492px;height:220px;background:linear-gradient(170deg,#b9cfe0,#5f8a6a 60%,#3f6a4d)" role="img" aria-label="Photograph of a lakeside alpine village"></div>
<div class="dest" style="left:604px;top:2000px;width:244px;height:220px;background:linear-gradient(170deg,#7fb3e0,#e9e6e0 50%,#c98a6c)" role="img" aria-label="Photograph of a whitewashed hillside town by the sea"></div>
<div class="dest" style="left:868px;top:2000px;width:244px;height:220px;background:linear-gradient(170deg,#a8c2d6,#8a9a5a 55%,#5b6e3a)" role="img" aria-label="Photograph of terraced mountain farmland"></div>
<div class="dest" style="left:88px;top:2232px;width:252px;height:220px;background:linear-gradient(170deg,#c9d6e2,#b07a5c 55%,#6e4a3a)" role="img" aria-label="Photograph of a historic European town square"></div>
<div class="dest" style="left:352px;top:2232px;width:496px;height:220px;background:linear-gradient(170deg,#a3b0bb,#8b8578 50%,#5b5a52)" role="img" aria-label="Photograph of a canyon landscape from above"></div>
<span class="dest-link"><svg width="18" height="18" viewBox="0 0 24 24" fill="none" stroke="#1c1c1c" stroke-width="2.2"><path d="M10 14a4 4 0 006 0l3-3a4 4 0 00-6-6l-1 1M14 10a4 4 0 00-6 0l-3 3a4 4 0 006 6l1-1"/></svg></span>
<div class="dest" style="left:868px;top:2232px;width:244px;height:220px;background:linear-gradient(170deg,#bcd3e6,#6f9a5c 55%,#3c5a34)" role="img" aria-label="Photograph of green hills and a river valley"></div>

<h2 class="section-title" style="top:2532px">Our Locations</h2>
<div class="abs world-map" role="img" aria-label="World map area marking popular destinations and business resource cities"></div>
<svg class="abs" style="left:0;top:2600px" width="1200" height="400" fill="none">
  <path d="M168 100a24 24 0 0148 0c0 20-24 46-24 46s-24-26-24-46z" fill="#27b1b4"/><circle cx="192" cy="100" r="9" fill="#fff"/>
  <path d="M404 260a24 24 0 0148 0c0 20-24 46-24 46s-24-26-24-46z" fill="#1a67c9"/><circle cx="428" cy="260" r="9" fill="#fff"/>
  <path d="M576 152a24 24 0 0148 0c0 20-24 46-24 46s-24-26-24-46z" fill="#7cb342"/><circle cx="600" cy="152" r="9" fill="#fff"/>
  <path d="M844 48a24 24 0 0148 0c0 20-24 46-24 46s-24-26-24-46z" fill="#f07c3a"/><circle cx="868" cy="48" r="9" fill="#fff"/>
  <path d="M1004 320a24 24 0 0148 0c0 20-24 46-24 46s-24-26-24-46z" fill="#9abb3a"/><circle cx="1028" cy="320" r="9" fill="#fff"/>
</svg>
<ul class="city-col" style="left:140px"><li>Shanghai</li><li>Beijing</li><li>Shenzhen</li><li>Guangzhou</li><li>Chongqing</li><li>Chengdu</li><li>Hangzhou/Jiangin</li><li>Xi'an</li><li>Nanjing</li></ul>
<ul class="city-col" style="left:368px"><li>Changchun</li><li>Wuhan</li><li>Fuzhou</li><li>Suzhou</li><li>Qingdao</li><li>Changsha</li><li>Jinan</li><li>Shenyang</li><li>Dongguan</li></ul>
<ul class="city-col" style="left:568px"><li>Lanzhou</li><li>Hefei</li><li>Guilin</li><li>Nanning</li><li>Nanchang</li><li>Harbin</li><li>Dalian</li><li>Nantong</li><li>Ningbo</li></ul>
<ul class="city-col" style="left:752px"><li>Taiyuan</li><li>Changzhou</li><li>Baotou</li><li>Kunming</li><li>Ningbo</li><li>Chongqing</li><li>Shijiazhuang</li><li>Xiamen</li><li>Harbin</li></ul>
<ul class="city-col" style="left:944px"><li>Changchun</li><li>Wuhan</li><li>Fuzhou</li><li>Suzhou</li><li>Qingdao</li><li>Changsha</li><li>Jinan</li><li>Shenyang</li><li>Dongguan</li></ul>

<div class="abs quote-mark">&ldquo;</div>
<h2 class="abs testi-title">What Our Client Say</h2>
<p class="abs testi-text">Lorem Ipsum is simply dummy text of the printing and typesetting industry. Lorem Ipsum has been the industry's standard dummy text ever since...</p>
<svg class="abs stars" width="90" height="14" viewBox="0 0 90 14" fill="#f2b62b"><path id="st" d="M7 0l2 5h5l-4 3 2 6-5-4-5 4 2-6-4-3h5z"/><use href="#st" x="18"/><use href="#st" x="36"/><use href="#st" x="54"/><use href="#st" x="72"/></svg>
<p class="abs testi-name">Mara Lindqvist</p>
<div class="abs client-photo" role="img" aria-label="Photograph of a traveller with a backpack looking over a lake"></div>

<footer class="abs site-footer"></footer>
<div class="abs cta"><h2>GET IN TOUCH WITH US</h2><span class="cta-btn">CONTACT US</span></div>
<div class="abs foot-brand"><span class="brand-dot"></span><span class="brand-name">Pelican Global<br>Trade &amp; Heritage Forum</span></div>
<div class="abs socials"><span></span><span></span><span></span><span></span></div>
<div class="foot-col" style="left:400px"><h3>Quick links</h3>Home<br>Tours<br>Destination<br>About<br>News<br>Contact</div>
<div class="foot-col" style="left:568px;width:200px"><h3>Contact info</h3>
  <div class="contact-row"><i></i><span>Email<br>hello@pelicanglobal.example</span></div>
  <div class="contact-row"><i></i><span>Phone<br>+1-555-0148-220</span></div>
  <div class="contact-row"><i></i><span>Location<br>Lorem ipsum is simply dummy text, United Kingdom</span></div>
</div>
<div class="foot-col" style="left:832px;width:300px"><h3>Newsletter</h3>Join our mailing list to hear about our latest projects and product offerings.
  <div class="newsletter">Enter your email...<b><svg width="16" height="16" viewBox="0 0 24 24" fill="#fff"><path d="M2 21l21-9L2 3v7l15 2-15 2z"/></svg></b></div>
</div>
<p class="abs copyright">&copy; 2023. All Rights Reserved | Pelican Global Trade &amp; Heritage Forum</p>
<span class="abs to-top"><svg width="14" height="14" viewBox="0 0 24 24" fill="none" stroke="#fff" stroke-width="3"><path d="M5 15l7-7 7 7"/></svg></span>

</body>
</html>
```